Redesign existing website.

I need a holidayhouse webdisain. Please review existing website: www.vaskemetsa.ee
I want to keep my logo.
Target Market(s)
Nature and sea enjoying holidaymakers, aged 30 to 70
Requirements
Must have
- 3 languages (English, Russian and Estonian)

```html
<!DOCTYPE html>
<html lang="et">
<head>
<meta charset="utf-8">
<title>Vaskemetsa Puhkemaja</title>
<link href="https://fonts.googleapis.com/css2?family=PT+Sans:wght@400;700&family=Open+Sans:wght@300;400&display=swap" rel="stylesheet">
<style>
  :root {
    --sky-top: #3f8fb4;
    --sky-mid: #7fb9c4;
    --meadow: #5d8a4a;
    --meadow-light: #a6b94a;
    --wood-dark: #4a2412;
    --wood: #7b3f1f;
    --wood-light: #a45a2c;
    --panel: rgba(205, 232, 228, 0.62);
    --panel-edge: rgba(235, 248, 246, 0.7);
    --band: rgba(40, 62, 52, 0.88);
    --caption: rgba(35, 45, 40, 0.85);
    --text-dark: #3a4a44;
    --text-light: #f4efe6;
    --text-muted: #d8c2a6;
    --logo-blue: #1a8fd0;
  }
  * { box-sizing: border-box; margin: 0; padding: 0; }
  html, body { width: 1110px; height: 1200px; overflow: hidden; }
  body {
    position: relative;
    font-family: "PT Sans", sans-serif;
    color: var(--text-dark);
  }
  .backdrop {
    position: absolute; inset: 0;
    background: linear-gradient(180deg, var(--sky-top) 0%, var(--sky-mid) 35%, #6aa3a0 60%, #4f7f6c 82%, var(--meadow-light) 90%, var(--meadow) 100%);
  }
  .brand {
    position: absolute; left: 108px; top: 58px;
    display: flex; align-items: center; gap: 8px;
    font-weight: 700; font-size: 16px;
    color: var(--text-light);
  }
  .brand-dot { width: 22px; height: 22px; border-radius: 50%; background: var(--logo-blue); }
  .main-nav {
    position: absolute; left: 297px; top: 0; width: 697px; height: 69px;
    background: linear-gradient(180deg, var(--wood-light), var(--wood) 60%, var(--wood-dark));
    border-radius: 0 0 12px 12px;
    box-shadow: 0 3px 6px rgba(0,0,0,.35);
  }
  .main-nav ul {
    position: absolute; left: 20px; right: 9px; top: 26px; height: 29px;
    display: flex; justify-content: space-between; align-items: center;
    list-style: none; padding: 0 10px;
    background: rgba(60, 28, 12, .45);
  }
  .main-nav a { color: var(--text-light); text-decoration: none; font-size: 14px; opacity: .85; }
  .main-nav a.active { opacity: 1; }
  .lang-switch {
    position: absolute; right: 105px; top: 112px;
    display: flex; gap: 4px; list-style: none;
  }
  .lang-switch a {
    display: block; width: 30px; height: 22px; line-height: 22px; text-align: center;
    font-size: 12px; font-weight: 700; color: var(--text-light); text-decoration: none;
    background: rgba(74, 36, 18, .7); border-radius: 3px;
  }
  .lang-switch a.current { background: var(--wood-light); }
  .content-panel {
    position: absolute; left: 102px; top: 148px; width: 903px; height: 580px;
    background: var(--panel);
    border: 1px solid var(--panel-edge);
  }
  .slider {
    position: absolute; left: 6px; top: 6px; width: 890px; height: 273px;
    background: linear-gradient(180deg, #9aa2a0 0%, #7f9aa2 28%, #c9bb9a 40%, #5c7d3c 60%, #3f5e2a 100%);
  }
  .slider-caption {
    position: absolute; left: 0; bottom: 0; width: 100%; height: 47px;
    background: var(--caption);
    color: #fff; font-size: 19px; text-align: center; line-height: 47px;
  }
  .arrow { position: absolute; width: 36px; height: 36px; }
  .welcome-tab {
    position: absolute; left: 0; top: 317px; width: 129px; height: 42px;
    background: linear-gradient(180deg, var(--wood-light) 0 22%, #c8884c 22%, #b0723c);
    border-radius: 0 10px 10px 0;
    font-family: "Open Sans", sans-serif; font-weight: 300; font-size: 27px;
    color: #fdf4e4; padding: 8px 0 0 8px; line-height: 1.1;
  }
  .intro {
    position: absolute; left: 32px; top: 378px; width: 850px;
    font-size: 13px; line-height: 15px;
  }
  .intro p + p { margin-top: 15px; }
  .gallery {
    position: absolute; left: 102px; top: 776px; width: 903px; height: 242px;
    background: var(--band);
  }
  .thumb { position: absolute; top: 29px; width: 247px; height: 184px; }
  .thumb.house { left: 56px; background: linear-gradient(180deg, #c9d9c4 0%, #7f9f7a 45%, #eef0ea 60%, #5d8a3a 100%); }
  .thumb.bedroom { left: 323px; background: linear-gradient(180deg, #e9e6de 0%, #d8d3c8 55%, #3d5fa8 80%, #2f4a86 100%); }
  .thumb.terrace { left: 587px; background: linear-gradient(180deg, #dfe6ea 0%, #7fa9c0 35%, #cfa67a 60%, #2f8fd0 100%); }
  .site-footer {
    position: absolute; left: 0; top: 1108px; width: 1110px; height: 92px;
    background: linear-gradient(180deg, var(--wood-dark) 0 4px, var(--wood-light) 4px, var(--wood) 60%, var(--wood-dark));
    color: var(--text-light);
  }
  .footer-contact { position: absolute; left: 22px; top: 16px; font-size: 11px; line-height: 15px; color: var(--text-muted); }
  .footer-contact h2 { font-size: 15px; font-weight: 400; color: #fff; margin-bottom: 2px; }
  .footer-nav { position: absolute; left: 314px; top: 28px; display: flex; gap: 50px; list-style: none; }
  .footer-nav li { font-size: 11px; text-transform: uppercase; }
  .copyright { position: absolute; left: 485px; top: 72px; font-size: 11px; color: var(--text-muted); }
  .follow { position: absolute; left: 958px; top: 24px; text-align: center; }
  .follow span { font-size: 13px; color: var(--text-muted); display: block; margin-bottom: 8px; }
  .social { display: flex; gap: 8px; }
  .social i { width: 34px; height: 34px; border-radius: 50%; display: block; }
  .social .one { background: #4ab0e0; }
  .social .two { background: #3a5ea0; }
  .social .three { background: #d04a32; }
</style>
</head>
<body>
  <div class="backdrop" role="img" aria-label="Sky with clouds, tree foliage at the edges and a green meadow below"></div>

  <div class="brand"><span class="brand-dot"></span>Vaskemetsa</div>

  <nav class="main-nav">
    <ul>
      <li><a class="active" href="#">TUTVUSTUS</a></li>
      <li><a href="#">HINNAKIRI</a></li>
      <li><a href="#">ASUKOHT</a></li>
      <li><a href="#">GALERII</a></li>
      <li><a href="#">HUVITAUT</a></li>
      <li><a href="#">KONTAKAT</a></li>
    </ul>
  </nav>

  <ul class="lang-switch" aria-label="Language">
    <li><a class="current" href="#" lang="et">ET</a></li>
    <li><a href="#" lang="en">EN</a></li>
    <li><a href="#" lang="ru">RU</a></li>
  </ul>

  <main class="content-panel">
    <div class="slider" role="img" aria-label="Beach with palm trees, a stone bench on the grass and the sea">
      <svg class="arrow" style="left:22px;top:142px" viewBox="0 0 36 36"><circle cx="18" cy="18" r="16.5" fill="rgba(0,0,0,.2)" stroke="#fff" stroke-width="2"/><path d="M21 10 L12 18 L21 26" fill="none" stroke="#fff" stroke-width="3"/></svg>
      <svg class="arrow" style="left:832px;top:142px" viewBox="0 0 36 36"><circle cx="18" cy="18" r="16.5" fill="rgba(0,0,0,.2)" stroke="#fff" stroke-width="2"/><path d="M15 10 L24 18 L15 26" fill="none" stroke="#fff" stroke-width="3"/></svg>
      <div class="slider-caption">Teid ootab mugav 2 magamistoaga puhkemaja</div>
    </div>

    <h1 class="welcome-tab">Welcome</h1>

    <div class="intro">
      <p>Majutus 5-le puhkajale. Teid ootab mugav 2 magamistoaga puhkemaja. Asume põhjarannikul, Juminda poolsaarel, Metsa külas, Lahemaa rahvuspargis. Tallinnast vaid 61 km kaugusel. Metsa on sobiv koht mõnusaks, rahulikuks puhkuseks. Sillerdavat merd ja kauneid päikeseloojanguid võib nautida lausa maja aknast. Või veel parem – jalutad randa ja istud päevapäikese poolt kuumaks köetud kivile. Meie maja vastas olev rand on kivine, väikesele liivarannale 100m. Lahemaa toredad terviserajad on lähedal.</p>
      <p>Alumisel korrusel elutuba kamina ja kööginurgaga. Kööginurgas kõik vajalik toidu valmistamiseks - elektripliit, nõudepesumasin, mikrolaineahi, külmik, kohvimasin, veekeetja, nõud. Maja II-l korrusel on kaks magamistuba, duširuum pesumasinaga, WC. Merepoolses toas paarisvoodi, lisaks diivanvoodi. Teises toas 2 voodit ja lahtikäiv tugitool.</p>
      <p>Pidustusteks puhkemaja välja ei rendita.</p>
    </div>
  </main>

  <section class="gallery">
    <svg class="arrow" style="left:10px;top:119px" viewBox="0 0 36 36"><circle cx="18" cy="18" r="16.5" fill="none" stroke="#fff" stroke-width="2"/><path d="M21 10 L12 18 L21 26" fill="none" stroke="#fff" stroke-width="3"/></svg>
    <div class="thumb house" role="img" aria-label="Holiday house with a white veranda among palm trees"></div>
    <div class="thumb bedroom" role="img" aria-label="Bedroom with a double bed and a window"></div>
    <div class="thumb terrace" role="img" aria-label="Sun loungers on a terrace facing the sea"></div>
    <svg class="arrow" style="left:851px;top:119px" viewBox="0 0 36 36"><circle cx="18" cy="18" r="16.5" fill="none" stroke="#fff" stroke-width="2"/><path d="M15 10 L24 18 L15 26" fill="none" stroke="#fff" stroke-width="3"/></svg>
  </section>

  <footer class="site-footer">
    <div class="footer-contact">
      <h2>VASKEMETSA PUHKEMAJA</h2>
      Ranna talu, Metsa küla, Tammiku vald, Harjumaa 74999<br>
      Tel. +372 55 01 234<br>
      e-mail: info@vaskemetsa.ee
    </div>
    <ul class="footer-nav">
      <li>Tutvustus</li><li>Hinnakiri</li><li>Asukoht</li><li>Galerii</li><li>Huvitaut</li><li>Kontakat</li>
    </ul>
    <div class="copyright">2014 All Rights Reserved</div>
    <div class="follow">
      <span>FOLLOW US</span>
      <div class="social"><i class="one"></i><i class="two"></i><i class="three"></i></div>
    </div>
  </footer>
</body>
</html>
```